Maple Lodging Hub website, brand new company, that rents rooms out in houses to milleniuls

We have a site right now that is weak as heck! We could use some punching it up. So we want it to be fun and cool, with added items in for social media (just twitter now) and anything else you want to throw at us. We do have a “blog” in there dedicated to events (we throw a lot of them) so want to incorporate that. Also have an existing design for a hand out that we want to use as our launching pad for colors… you can deviate from it a bit though.

Target Market(s)

25-40 year olds transitioning to the city from other places in the country. Millennial are the min group

Industry/Entity Type

Real Estate

Coding

Coded - Design and coding required

Number of Pages Required

5+ page

Font styles to use
Sans Serif

Requirements
Must have
• Fun look, same pages as those uploaded, but not necessarily the look and feel of what we have already.
• Follow the content of our posted site www.MapleLodgingHub.example
• FOOTER
• LOGO | SITEMAP | SOCIAL LINKS | MAIN CTA REMINDER | CONTACT INFO | COPYRIGHT INFO | TERMS AND CONDITIONS
Nice to have
• Use as many of my graphics as loaded, but feel free to use stock photos as well interlaced. Including both people in their 20’s, 30’s, 40’s, having a fun time or of nice houses, inside and out.

```html
<!DOCTYPE html>
<html lang="en">
<head>
<meta charset="utf-8">
<title>Maple Lodging Hub</title>
<link href="https://fonts.googleapis.com/css2?family=Raleway:wght@500;600;700;800&family=Open+Sans:wght@400;600;700&display=swap" rel="stylesheet">
<style>
:root{
  --blue:#0a5fc4;
  --blue-dark:#084fa5;
  --sky:#5b98d8;
  --ink:#1d1d1d;
  --text:#555;
  --muted:#8a8a8a;
  --light:#f4f4f4;
  --footer:#222;
  --black:#111;
  --white:#fff;
}
*{margin:0;padding:0;box-sizing:border-box}
html,body{width:1200px;height:3734px;overflow:hidden}
body{position:relative;font-family:"Open Sans",Arial,sans-serif;color:var(--text);background:var(--white)}
.abs{position:absolute}
h1,h2,h3,.heading{font-family:"Raleway","Open Sans",sans-serif}

/* top bar */
.topbar{left:0;top:0;width:1200px;height:30px;background:var(--black);color:var(--white);font-size:11px;font-weight:600}
.topbar .welcome{left:60px;top:8px}
.topbar .social{right:80px;top:8px;display:flex;gap:25px}
.topbar .social span{width:13px;height:13px;background:#e8e8e8;border-radius:2px;display:block}

/* header */
.brand{display:flex;align-items:center;gap:10px;font-family:"Raleway",sans-serif;font-weight:800;color:var(--blue);font-size:27px;letter-spacing:.5px}
.brand .mark{width:22px;height:22px;background:var(--blue);display:block}
.header .brand{left:60px;top:84px}
.contact-item{display:flex;gap:12px;align-items:center;font-size:13px;color:#333;line-height:1.15}
.header .addr{left:727px;top:76px}
.header .phone{left:978px;top:76px}

/* nav */
.nav{left:0;top:150px;width:1200px;height:45px;background:var(--blue);display:flex;padding-left:60px}
.nav a{display:block;color:var(--white);text-decoration:none;font-size:12.5px;font-weight:600;text-transform:uppercase;padding:0 15px;line-height:45px}
.nav a.active{background:#0c2c55}

/* hero */
.hero{left:0;top:195px;width:1200px;height:515px;background:linear-gradient(180deg,#c7ccd2 0%,#b9bec5 45%,#8a8279 75%,#6f655b 100%)}
.hero-title{left:269px;top:161px;width:690px;height:92px;background:rgba(34,34,34,.88);color:var(--white);font-family:"Raleway",sans-serif;font-weight:700;font-size:38px;display:flex;align-items:center;justify-content:center;letter-spacing:1px}
.btn{display:flex;align-items:center;justify-content:center;background:var(--blue);color:var(--white);font-size:13px;font-weight:600}
.hero .btn{left:518px;top:278px;width:154px;height:47px;font-size:16px;font-weight:400}
.hero-arrow{top:240px;width:28px;height:28px;border-radius:50%;background:#2a2a2a;display:flex;align-items:center;justify-content:center}
.hero-arrow.left{left:28px}.hero-arrow.right{right:28px}

/* section headings */
.sec-title{width:1200px;text-align:center;font-family:"Raleway",sans-serif;font-weight:700;font-size:37px;color:var(--black)}
.sec-sub{width:1200px;text-align:center;font-size:12px;color:#666}

/* about */
.about-text{left:160px;top:871px;width:880px;text-align:center;font-size:12.5px;line-height:23px;color:#666}

/* founder */
.founder-photo{left:0;top:1001px;width:573px;height:339px;background:linear-gradient(120deg,#3b5a7a 0%,#8397ad 45%,#cfd6dd 100%)}
.founder-panel{left:573px;top:1001px;width:627px;height:339px;background:var(--blue);color:var(--white)}
.founder-panel h2{position:absolute;left:32px;top:40px;font-size:24px;font-weight:700}
.founder-panel p{position:absolute;left:32px;top:85px;width:560px;font-size:12.5px;line-height:21px;font-weight:600}
.founder-panel .btn-white{position:absolute;left:37px;top:231px;width:142px;height:51px;background:var(--white);color:#222;font-weight:700;font-size:14px;display:flex;align-items:center;justify-content:center}

/* why */
.why{left:0;top:1340px;width:1200px;height:565px;background:var(--light)}
.why-col{width:270px;text-align:center;top:204px}
.why-col h3{font-size:14px;font-weight:700;color:#222;text-transform:uppercase;margin-top:18px;letter-spacing:.3px}
.why-col p{font-size:12px;line-height:19px;color:#777;margin:8px 10px 0}
.why-col .btn{width:98px;height:44px;margin:14px auto 0;font-size:12px}
.why-arrow{top:273px}

/* events */
.events-title{left:60px;top:1962px;font-family:"Raleway",sans-serif;font-weight:700;font-size:26px;color:var(--black)}
.events-rule{left:60px;top:2002px;width:62px;height:4px;background:var(--blue)}
.tabs{right:60px;top:1970px;display:flex;gap:36px;font-size:16px;font-weight:700;color:var(--black)}
.tabs .on{color:var(--blue)}
.card{width:328px;height:231px}
.card .photo{position:absolute;left:0;top:0;width:100%;height:186px}
.card .cap{position:absolute;left:0;bottom:0;width:100%;height:45px;background:var(--blue);color:var(--white);font-weight:700;font-size:15px;display:flex;align-items:center;justify-content:center}
.card.all .overlay{position:absolute;inset:0;background:rgba(20,70,140,.78);display:flex;flex-direction:column;align-items:center;justify-content:center;color:var(--white);font-weight:600;font-size:15px;gap:6px}
.dots{left:580px;top:2621px;display:flex;gap:4px}
.dots span{width:12px;height:12px;border-radius:50%;background:#333}
.dots span:first-child{background:var(--blue)}

/* fans */
.fans{left:0;top:2684px;width:1200px;height:416px;background:var(--sky)}
.fans .sec-title{color:var(--white);top:54px;font-size:38px}
.quote{left:120px;top:135px;width:951px;height:157px;background:var(--blue);color:var(--white);font-size:15px;line-height:26px;text-align:center;padding:28px 60px}
.fan-arrow{top:188px;width:48px;height:48px;border-radius:50%;border:2px solid rgba(255,255,255,.8);display:flex;align-items:center;justify-content:center}
.fan-arrow.left{left:10px}.fan-arrow.right{right:10px}
.author{left:520px;top:323px;display:flex;align-items:center;gap:14px;font-size:12px;color:#2b3d55}
.author .avatar{width:46px;height:46px;border-radius:50%;background:linear-gradient(135deg,#c8a88c,#7b5a45)}

/* map */
.map{left:0;top:3100px;width:1200px;height:192px;background:linear-gradient(180deg,#ece6d9,#e1dccd)}

/* footer */
.footer{left:0;top:3292px;width:1200px;height:401px;background:var(--footer);color:#bbb}
.footer .brand{position:absolute;left:60px;top:40px;font-size:24px}
.footer .about{position:absolute;left:60px;top:160px;width:240px;font-size:12.5px;line-height:22px;color:#bbb}
.footer .social{position:absolute;left:60px;top:298px;display:flex;gap:7px}
.footer .social span{width:24px;height:24px;display:block;background:#3a72c4}
.footer .social span:nth-child(even){background:#2b5ea8}
.footer h4{font-family:"Raleway",sans-serif;font-size:19px;font-weight:600;color:var(--white)}
.twitter{left:468px;top:56px;width:260px}
.tweet{display:flex;gap:10px;margin-top:30px;font-size:12.5px;line-height:21px;color:#ddd}
.tweet:first-of-type{margin-top:36px}
.tweet .dot{flex:none;width:12px;height:12px;border-radius:50%;background:#4a9ae8;margin-top:5px}
.tweet b{color:var(--white)}
.tweet .link{font-weight:700;color:var(--white)}
.tweet-rule{height:1px;background:#3a3a3a;margin-top:22px}
.contact{left:839px;top:56px;width:300px;font-size:12.5px;line-height:20px;color:#ddd}
.contact .dim{color:#888}
.contact .gap{margin-top:20px}
.contact b{color:var(--white);font-weight:600}
.copyright{left:0;top:3693px;width:1200px;height:41px;background:var(--black);color:#bbb;font-size:12px;display:flex;align-items:center;justify-content:center}
</style>
</head>
<body>

<div class="abs topbar">
  <div class="abs welcome">Welcome visitor</div>
  <div class="abs social" aria-label="Social links"><span></span><span></span><span></span><span></span><span></span></div>
</div>

<header class="header">
  <div class="abs brand"><span class="mark"></span>Maple Lodging Hub</div>
  <div class="abs contact-item addr">
    <svg width="38" height="34" viewBox="0 0 38 34" fill="none" stroke="#0a5fc4" stroke-width="2.4"><path d="M3 17 19 3l16 14"/><path d="M8 13v18h22V13"/><path d="M16 31v-9h6v9"/></svg>
    <div>Albany, New York - 12207<br>United States</div>
  </div>
  <div class="abs contact-item phone">
    <svg width="22" height="36" viewBox="0 0 22 36" fill="none" stroke="#0a5fc4" stroke-width="2.4"><rect x="2" y="2" width="18" height="32" rx="3"/><path d="M9 29h4"/></svg>
    <div>Phone : 555-0142-880</div>
  </div>
</header>

<nav class="abs nav">
  <a class="active">Home</a><a>Our Communities</a><a>Ammenities</a><a>Fitting</a><a>Events</a><a>About Us</a><a>Contact</a>
</nav>

<section class="abs hero" role="img" aria-label="Photo of a modern white house with a wooden deck at dusk">
  <div class="abs hero-title">EXPERIENCE THE DIFFERENCE</div>
  <div class="abs btn">Read More</div>
  <div class="abs hero-arrow left"><svg width="12" height="12" viewBox="0 0 12 12"><path d="M8 1 3 6l5 5" stroke="#fff" stroke-width="2" fill="none"/></svg></div>
  <div class="abs hero-arrow right"><svg width="12" height="12" viewBox="0 0 12 12"><path d="M4 1l5 5-5 5" stroke="#fff" stroke-width="2" fill="none"/></svg></div>
</section>

<h1 class="abs sec-title" style="left:0;top:763px">ABOUT THE COMMUNITY</h1>
<div class="abs sec-sub" style="left:0;top:820px">Saving money is just a nice perk</div>
<p class="abs about-text">When our founder moved to Charlotte it was a majortransition period in his life— right in the middle of a slew ofmajor life changes. He picked up a new job, went to a new city,starting over with friends, and trying to start a new life.One of the first things he did bought a big house.<br>he did bought a big house.</p>

<div class="abs founder-photo" role="img" aria-label="Photo of a speaker in a suit talking with a guest at a conference"></div>
<section class="abs founder-panel">
  <h2>When our founder moved to Charlotte</h2>
  <p>When our founder moved to Charlotte it was a majortransition period in his life— right in the middle of a slew ofmajor life changes. He picked up a new job, went to a new city, starting over with friends, and trying to start a new life.One of the first things he did—bought a big house.<br>Feeling somewhat isolated, he naturally started looking for like-kind people to share his home with. One room at a time.</p>
  <div class="btn-white">Read More</div>
</section>

<section class="abs why">
  <h2 class="abs sec-title" style="left:0;top:60px">WHY BE A PART OF OUR COMMUNITY?</h2>
  <div class="abs sec-sub" style="left:0;top:107px">Saving money is just a nice perk</div>
  <svg class="abs why-arrow" style="left:42px" width="14" height="22" viewBox="0 0 14 22"><path d="M11 2 3 11l8 9" stroke="#111" stroke-width="3" fill="none"/></svg>
  <svg class="abs why-arrow" style="left:1142px" width="14" height="22" viewBox="0 0 14 22"><path d="M3 2l8 9-8 9" stroke="#111" stroke-width="3" fill="none"/></svg>

  <div class="abs why-col" style="left:39px;top:202px">
    <svg width="80" height="122" viewBox="0 0 80 122"><path d="M40 2C19 2 2 19 2 40c0 28 38 80 38 80s38-52 38-80C78 19 61 2 40 2z" fill="#0a5fc4"/><circle cx="40" cy="38" r="11" fill="none" stroke="#fff" stroke-width="3"/><path d="M35 52h10" stroke="#fff" stroke-width="3"/></svg>
    <h3>Inspiration and Motivation</h3>
    <p>in strong communities there is always some-one doing somethingamazing (if not many people), if not organically</p>
    <div class="btn">Read More</div>
  </div>
  <div class="abs why-col" style="left:321px;top:202px">
    <svg width="80" height="122" viewBox="0 0 80 122"><path d="M40 2C19 2 2 19 2 40c0 28 38 80 38 80s38-52 38-80C78 19 61 2 40 2z" fill="#0a5fc4"/><rect x="29" y="25" width="22" height="28" rx="2" fill="none" stroke="#fff" stroke-width="3"/><path d="M34 34h12M34 41h12" stroke="#fff" stroke-width="2.5"/></svg>
    <h3>Shared Lessons</h3>
    <p>in strong communities there is always some-one doing somethingamazing (if not many people), if not organically</p>
    <div class="btn">Read More</div>
  </div>
  <div class="abs why-col" style="left:590px;top:202px">
    <svg width="80" height="122" viewBox="0 0 80 122"><path d="M40 2C19 2 2 19 2 40c0 28 38 80 38 80s38-52 38-80C78 19 61 2 40 2z" fill="#0a5fc4"/><circle cx="33" cy="33" r="6" fill="#fff"/><circle cx="48" cy="33" r="6" fill="#fff"/><path d="M22 52c0-8 5-12 11-12s11 4 11 12zM37 52c0-8 5-12 11-12s11 4 11 12z" fill="#fff"/></svg>
    <h3>Contacts</h3>
    <p>in strong communities there is always some-one doing somethingamazing (if not many people), if not organically</p>
    <div class="btn">Read More</div>
  </div>
  <div class="abs why-col" style="left:861px;top:202px">
    <svg width="80" height="122" viewBox="0 0 80 122"><path d="M40 2C19 2 2 19 2 40c0 28 38 80 38 80s38-52 38-80C78 19 61 2 40 2z" fill="#0a5fc4"/><path d="M28 50 40 24l12 26z" fill="none" stroke="#fff" stroke-width="3"/><circle cx="40" cy="42" r="3" fill="#fff"/></svg>
    <h3>Opportunities</h3>
    <p>in strong communities there is always some-one doing somethingamazing (if not many people), if not organically</p>
    <div class="btn">Read More</div>
  </div>
</section>

<h2 class="abs events-title">EVENTS FOR ALL</h2>
<div class="abs events-rule"></div>
<div class="abs tabs"><span class="on">EVENTS</span><span>AMMENITIES</span><span>OTHER PERKS?</span><span>OUR COMMUNITIES</span></div>

<div class="abs card" style="left:60px;top:2084px"><div class="photo" role="img" aria-label="Photo of friends in party hats posing at an event" style="background:linear-gradient(135deg,#7a2b2b,#2a1f1f)"></div><div class="cap">Event 1</div></div>
<div class="abs card" style="left:433px;top:2084px"><div class="photo" role="img" aria-label="Photo of a crowd gathered at a bar event" style="background:linear-gradient(135deg,#9a6a3c,#3e2a1f)"></div><div class="cap">Event 2</div></div>
<div class="abs card" style="left:812px;top:2084px"><div class="photo" role="img" aria-label="Photo of cyclists in helmets outdoors" style="background:linear-gradient(135deg,#6f8a4c,#2f3d22)"></div><div class="cap">Event 3</div></div>
<div class="abs card" style="left:60px;top:2351px"><div class="photo" role="img" aria-label="Photo of a group in suits at an evening event" style="background:linear-gradient(135deg,#8a6a4a,#2b2420)"></div><div class="cap">Event 4</div></div>
<div class="abs card all" style="left:433px;top:2351px"><div class="photo" role="img" aria-label="Photo of a group outdoors in matching shirts" style="background:linear-gradient(135deg,#5d8fb8,#2a4a6a);height:100%"></div>
  <div class="overlay"><svg width="26" height="26" viewBox="0 0 26 26"><path d="M13 2v22M2 13h22" stroke="#fff" stroke-width="4"/></svg>VIEW ALL</div></div>
<div class="abs card" style="left:812px;top:2351px"><div class="photo" role="img" aria-label="Photo of friends in party hats posing at an event" style="background:linear-gradient(135deg,#7a2b2b,#2a1f1f)"></div><div class="cap">Event 5</div></div>
<div class="abs dots"><span></span><span></span><span></span></div>

<section class="abs fans">
  <h2 class="abs sec-title" style="left:0">OUR FANS</h2>
  <div class="abs fan-arrow left"><svg width="12" height="14" viewBox="0 0 12 14"><path d="M9 1 3 7l6 6" stroke="#fff" stroke-width="2" fill="none"/></svg></div>
  <div class="abs fan-arrow right"><svg width="12" height="14" viewBox="0 0 12 14"><path d="M3 1l6 6-6 6" stroke="#fff" stroke-width="2" fill="none"/></svg></div>
  <blockquote class="abs quote">"I thought I wanted to live on my own, but the realityis I just didn't want to go through he hassle of findinga good room mate. Someone with common intereststhat's not out partying at night. I'm a professionaland don't need that in my life. Now I'm a part of agreat social, athletic, professional community thatencourages the most out of me"</blockquote>
  <div class="abs author"><div class="avatar" role="img" aria-label="Portrait photo of the reviewer"></div>Rory Bell,Blogger</div>
</section>

<div class="abs map" role="img" aria-label="Street map showing the community locations"></div>

<footer class="abs footer">
  <div class="brand"><span class="mark"></span>Maple Lodging Hub</div>
  <p class="about">This is the perfect four bedroom family home on an idyllic block, in one of Chicago's nicest suburbs. With three bedrooms and a master suite, there is plenty of space for all.</p>
  <div class="social" aria-label="Social links"><span></span><span></span><span></span><span></span><span></span><span></span><span></span></div>

  <div class="abs twitter">
    <h4>Twitter</h4>
    <div class="tweet"><span class="dot"></span><div><b>@MapleHub</b> come and pick one of our #CityLiving rooms on #NewInTown<br><span class="link">maplelodginghub.example/events</span></div></div>
    <div class="tweet-rule"></div>
    <div class="tweet"><span class="dot"></span><div><b>@MapleHub</b> Check out Rooftop Social - Fashion &amp; Lifestyle #RoomMates Blog on #MapleHub by @MapleHub #eventnight<br><span class="link">maplelodginghub.example/blog/...</span></div></div>
  </div>

  <div class="abs contact">
    <h4 style="margin-bottom:22px">Contact Us</h4>
    <p>48 Birchwood Lane<br>Albany, New York - 12207<br><span class="dim">United States</span></p>
    <p class="gap">Phone : 555-0142-880<br>Email : hello@maplelodginghub.example</p>
    <p class="gap"><span class="dim">Opening Hours</span><br><b>Monday - Friday : 9 am To 6 pm<br>Saturday - Sunday : 9 am To 2 pm</b></p>
  </div>
</footer>
<div class="abs copyright">© 2016 MAPLELODGINGHUB.EXAMPLE All Right Reserved.</div>

</body>
</html>
```